Scientific Poster- Immunology Marcus T

I have all the information, but need this placed in a design format where it can be printed. The size will need to be 1meter by 1 meter. I just have the basic text and images. I just need the design around that added to make it look more attractive.
Please see some of the examples online, with web link below.

Target Market(s)

Scientific Meeting

Font styles to use
Sans Serif

Requirements
Must have
• Professional appearance
Nice to have
• examples can be found on
• https://www.orvelmintprints.com/sample_gallery_pages
Should not have
• Should be professional

```html
<!DOCTYPE html>
<html lang="en">
<head>
<meta charset="utf-8">
<title>Image Guided Cryoablation with Intra-Tumor Checkpoint Inhibitors</title>
<link href="https://fonts.googleapis.com/css2?family=Arimo:ital,wght@0,400;0,700;1,400;1,700&family=Archivo:wght@800&display=swap" rel="stylesheet">
<style>
:root{
  --navy:#0f2f66;
  --navy-deep:#0a2150;
  --band:#1663b3;
  --band-light:#2f86d2;
  --canvas:#c4def3;
  --panel:#dbecf9;
  --panel-edge:#8fb3d3;
  --ink:#15253d;
  --case-ink:#27508f;
  --caption:#1a5aa6;
  --scan-dark:#1b1f2b;
  --scan-mid:#4c5568;
  --scan-pet:#26307a;
}
*{box-sizing:border-box;margin:0;padding:0}
html,body{width:1200px;height:1200px;overflow:hidden}
body{background:var(--canvas);font-family:"Arimo",Arial,sans-serif;color:var(--ink);position:relative}
.title-band{position:absolute;left:0;top:0;width:1200px;height:84px;background:linear-gradient(180deg,var(--navy) 0%,var(--navy-deep) 100%);border-bottom:3px solid #fff;display:flex;align-items:center;justify-content:center;text-align:center}
.title-band h1{font-family:"Archivo","Arimo",sans-serif;font-weight:800;color:#fff;font-size:26px;line-height:1.2;letter-spacing:.2px;text-transform:uppercase}
.authors{position:absolute;top:92px;left:0;width:1200px;display:flex;justify-content:space-around;padding:0 170px;font-size:15px;color:var(--ink)}
.abstract-tag{position:absolute;left:16px;top:118px;width:440px;height:30px;background:linear-gradient(90deg,var(--band) 60%,rgba(22,99,179,0));color:#fff;font-weight:700;font-size:24px;padding-left:10px;line-height:30px}
.section-head{position:absolute;left:0;width:1200px;height:22px;display:flex;align-items:center;justify-content:center}
.section-head::before{content:"";position:absolute;left:22px;right:22px;top:5px;height:12px;background:var(--band)}
.section-head span{position:relative;background:linear-gradient(180deg,var(--band-light),var(--band));color:#fff;font-weight:700;font-size:15px;padding:2px 0;width:340px;text-align:center;letter-spacing:.5px}
.section-text{position:absolute;left:26px;width:1148px;font-size:13.3px;line-height:1.3}
.hyp-head{top:136px}.hyp-text{top:166px}
.meth-head{top:230px}.meth-text{top:261px}
.res-head{top:373px}.res-text{top:404px}
.conc-head{top:1083px}.conc-text{top:1110px;font-size:13.8px}
.cases{position:absolute;left:8px;top:474px;width:1184px;height:604px;display:grid;grid-template-columns:392px 392px 392px;gap:4px}
.case{background:var(--panel);border:1px solid var(--panel-edge);display:flex;flex-direction:column}
.case-head{height:20px;background:linear-gradient(180deg,var(--band-light),var(--band));color:#fff;font-weight:700;font-size:15px;text-align:center;line-height:20px}
.case-intro{font-size:11.4px;line-height:1.22;color:var(--case-ink);padding:5px 8px 4px}
.figures{flex:1;display:grid;gap:6px 10px;padding:4px 10px 8px}
.case-1 .figures{grid-template-columns:1fr 1fr}
.case-2 .figures{grid-template-columns:1fr 1fr 1fr}
.case-3 .figures{grid-template-columns:1fr 1fr;padding:4px 26px 8px}
.figure{display:flex;flex-direction:column}
.scan{flex:1;min-height:40px;border:1px solid #7d8ea6}
.scan.pet{background:radial-gradient(ellipse at 50% 55%,#3a56b8 0%,var(--scan-pet) 55%,#0c0f2e 100%)}
.scan.ct{background:radial-gradient(ellipse at 50% 50%,#c9cbd0 0%,var(--scan-mid) 45%,var(--scan-dark) 80%)}
.scan.spine{background:radial-gradient(ellipse at 50% 55%,#8b8f97 0%,#555b66 40%,var(--scan-dark) 85%)}
.caption{background:var(--caption);color:#fff;font-style:italic;font-weight:700;font-size:8.6px;line-height:1.2;padding:3px 4px;min-height:44px}
</style>
</head>
<body>
<header class="title-band">
  <h1>Image Guided Cryoablation of Cancer with Intra-Tumor Injection<br>of Anti-CTLA-4 and PD-1 Immune Checkpoint Inhibitors</h1>
</header>
<div class="authors"><span>Marcus T. Williams MD</span><span>Daniel E. Hartwell MD</span><span>Owen A. Lindqvist MD</span></div>
<div class="abstract-tag">ABSTRACT:</div>

<div class="section-head hyp-head"><span>HYPOTHESIS:</span></div>
<p class="section-text hyp-text">In situ Image Guided Cancer Cryoablation combined with image guided injection of immune check-point inhibitors is an effective method of treating local and systemic malignancy. The inflammatory cytokines and release of tumor antigens from Cryoablation, combined with immune check-point inhibitors can create an in-situ tumor vaccine resulting in a systemic anti-cancer immune response.</p>

<div class="section-head meth-head"><span>METHODS:</span></div>
<p class="section-text meth-text">Patients participating in an ongoing research protocol underwent in situ Image Guided Cryoablation of one or more malignant cancers. Image guidance included Computed Tomography and or Ultrasound. The Cryoablation procedure was performed using standard well developed and described percutaneous techniques. For the procedure, each patient received either IV or general anesthesia. Immediately following the cryoablation of cancer, each cryo-treated tumor was injected with a combination of Ipilimumab/Nivolumab or Ipilimumab/Pembrolizumab immune checkpoint inhibitors. The injection was performed with 50% of the systemic dose of 3mg/kg. The patients remained monitored inpatients for 24-48 hours post surgery. Follow-up with serum tumor markers where applicable, CBC, and serum chemistries were obtained at 1 week and every month post procedure. Cross sectional Imaging was obtained at 3-4 weeks and at every 3 months post procedure.</p>

<div class="section-head res-head"><span>RESULTS:</span></div>
<p class="section-text res-text">Patients treated with in situ tumor cryoablation demonstrated the expected macro cellular cryo-necrosis with morphologic changes in the treated tissue, which was evident as early as 6 hours postop. With more time, the treated tumor morphology was noted to deviate from the standard cryoablation decay with some patients having rapid large volume tissue decay far exceeding that expected from cryoablation alone. In the non treated tumor as identified on cross sectional imaging, distant tumor deposits were noted to decrease in size and many to disappear. At 6 months post treatment there has been no recurrence of responding tumor.</p>

<main class="cases">
  <section class="case case-1">
    <div class="case-head">PATIENT #1</div>
    <p class="case-intro">Patient is a 58-year-old female with a seven-year history of tumor of unknown origin, presumed breast. She had prior standard of care treatment with chemotherapy and radiation. The patient had failed all standard options and continued to have progression with numerous tumors in the lungs and thoracic lymph nodes. The patient was then treated with image-guided ablation combined with Ipilimumab and Pembrolizumab.</p>
    <div class="figures">
      <figure class="figure"><div class="scan pet" role="img" aria-label="PET/CT scan with uptake in right upper lobe nodules"></div><figcaption class="caption">Image above demonstrates FDG PET/CT with abnormal uptake in two right upper lobe nodules.</figcaption></figure>
      <figure class="figure"><div class="scan pet" role="img" aria-label="PET/CT scan with uptake in hilar and peri-aortic lymph nodes"></div><figcaption class="caption">Image above demonstrates FDG PET/CT with abnormal uptake in bilateral infra-hilar and right peri-aortic lymph nodes.</figcaption></figure>
      <figure class="figure"><div class="scan pet" role="img" aria-label="PET/CT scan with uptake in supra-hilar and axillary lymph nodes"></div><figcaption class="caption">Image above demonstrates FDG PET/CT with abnormal uptake in right supra-hilar lymph nodes, right upper lobe nodule and right axillary lymph node.</figcaption></figure>
      <figure class="figure"><div class="scan ct" role="img" aria-label="CT scan during ablation with needle in right upper lobe lesion"></div><figcaption class="caption">Image above is a CT scan performed during the ablation procedure demonstrating ablation needle with a right upper lobe lesion.</figcaption></figure>
      <figure class="figure"><div class="scan pet" role="img" aria-label="PET/CT two months after treatment of ablated site"></div><figcaption class="caption">The image above demonstrates a FDG PET/CT scan performed 2 months after treatment with minimal peripheral FDG uptake of the ablated tumor site.</figcaption></figure>
      <figure class="figure"><div class="scan pet" role="img" aria-label="PET/CT two months after surgery showing reduced adenopathy"></div><figcaption class="caption">The above image is a FDG PET/CT performed 2 months after surgery showing resolution of infra-hilar adenopathy, with minimal residual uptake in peri-aortic adenopathy.</figcaption></figure>
    </div>
  </section>

  <section class="case case-2">
    <div class="case-head">PATIENT #2</div>
    <p class="case-intro">Patient is a 68 year old male with a 2 year history of a left renal mass. The patient underwent a left nephrectomy with a diagnosis of renal cell carcinoma. A subsequent CT scan demonstrated numerous lung nodules (&gt;20) and a large L5 vertebral body mass. The patient was then treated with Cryoablation of the L5 mass with intra-tumoral injection of Ipilimumab and Nivolumab into the ablated tumor site. A follow up CT scan 7 weeks after treatment demonstrated complete resolution of the lung nodules with a stable L5 mass.</p>
    <div class="figures">
      <figure class="figure"><div class="scan ct" role="img" aria-label="Chest CT with a lung nodule"></div><figcaption class="caption">The image above demonstrates a CT scan of the chest with a lung nodule.</figcaption></figure>
      <figure class="figure"><div class="scan ct" role="img" aria-label="Chest CT with multiple bilateral lung nodules"></div><figcaption class="caption">CT scan of the chest demonstrates multiple bilateral lung nodules.</figcaption></figure>
      <figure class="figure"><div class="scan ct" role="img" aria-label="Chest CT with additional lung nodule"></div><figcaption class="caption">CT scan of the chest demonstrating additional lung nodule.</figcaption></figure>
      <figure class="figure"><div class="scan spine" role="img" aria-label="Lumbar spine CT with L5 mass"></div><figcaption class="caption">CT scan of the lumbar spine demonstrating L5 mass.</figcaption></figure>
      <figure class="figure"><div class="scan spine" role="img" aria-label="CT during cryoablation of L5 mass"></div><figcaption class="caption">CT scan during ablation procedure demonstrating Cryoablation of L5 mass.</figcaption></figure>
      <figure class="figure"><div class="scan ct" role="img" aria-label="Chest CT seven weeks after procedure"></div><figcaption class="caption">CT scan 7 weeks after procedure demonstrating resolution of lung nodules.</figcaption></figure>
      <figure class="figure"><div class="scan ct" role="img" aria-label="Chest CT seven weeks after procedure"></div><figcaption class="caption">CT scan 7 weeks after procedure demonstrating resolution of lung nodules.</figcaption></figure>
      <figure class="figure"><div class="scan ct" role="img" aria-label="Chest CT seven weeks after procedure"></div><figcaption class="caption">CT scan 7 weeks after procedure demonstrating resolution of lung nodules.</figcaption></figure>
      <figure class="figure"><div class="scan spine" role="img" aria-label="Lumbar spine CT seven weeks after treatment"></div><figcaption class="caption">CT scan of the lumbar spine 7 weeks after treatment demonstrating stable lumbar mass.</figcaption></figure>
    </div>
  </section>

  <section class="case case-3">
    <div class="case-head">PATIENT #3</div>
    <p class="case-intro">Patient is a 54 year old female with a several year history of breast cancer who then developed non-small cell lung cancer. The patient underwent several years of treatment with standard chemotherapy and radiation. The patient then developed a new large lung mass with mediastinal adenopathy. A new biopsy was performed demonstrating malignancy of neuroendocrine type. The patient opted for no further chemotherapy, but did agree to Cryoablation combined with intra-tumoral injection of Ipilimumab and Nivolumab. Due to the large volume of tumor, only a small area of tumor was ablated and treated. However, by 2 months, the patient demonstrated a whole body systemic response with resolution of tumors beyond the ablation site. This further supports that ablation combined with immune checkpoint inhibitors can create a systemic, anti-tumor immune response, essentially an in-situ tumor vaccine.</p>
    <div class="figures">
      <figure class="figure"><div class="scan pet" role="img" aria-label="PET/CT with abnormal hilar and subcarinal lymph nodes"></div><figcaption class="caption">Image demonstrates PET/CT with abnormal right hilar and subcarinal lymph nodes.</figcaption></figure>
      <figure class="figure"><div class="scan ct" role="img" aria-label="CT with large mediastinal and right hilar mass"></div><figcaption class="caption">Image demonstrates a large mediastinal and right hilar mass prior to the Cryoablation procedure combined with immune checkpoint injection.</figcaption></figure>
      <figure class="figure"><div class="scan ct" role="img" aria-label="CT of cryoablation needle in subcarinal lymph node"></div><figcaption class="caption">Image demonstrates Cryoablation procedure with the needle placed within the subcarinal lymph node.</figcaption></figure>
      <figure class="figure"><div class="scan ct" role="img" aria-label="CT of treated subcarinal lymph node after cryoablation"></div><figcaption class="caption">Image demonstrates normal expected low attenuation with the treated subcarinal lymph node, which is a typical post Cryoablation appearance.</figcaption></figure>
      <figure class="figure"><div class="scan ct" role="img" aria-label="One month follow up CT"></div><figcaption class="caption">One month follow up CT demonstrates significant reduction in the associated mediastinal and right hilar mass.</figcaption></figure>
      <figure class="figure"><div class="scan pet" role="img" aria-label="Two month follow up PET/CT"></div><figcaption class="caption">Two month follow up PET/CT shows resolution of mediastinal and right hilar masses.</figcaption></figure>
    </div>
  </section>
</main>

<div class="section-head conc-head"><span>CONCLUSION:</span></div>
<p class="section-text conc-text">The combination of intra-tumoral checkpoint inhibitor injection with percutaneous cryoablation of metastatic malignancy shows great promise in providing a far superior treatment methodology than either method alone, has previously shown. It has been known that ablation techniques, especially Cryoablation can generate an anti-tumor immune response; however, this is rarely curative. These cases show that the combination of immune checkpoint inhibitors with Cryoablation generates a synergy, effectively creating a tumor vaccine, which can cause the resolution of not only the local treated area, but also a systemic response eradicating all visible disease. Further data from this study will better refine this conclusion.</p>
</body>
</html>
```